Business Card Design job - Tessa's Business Cards

Simple elegant feminine design - Going out on my own as a Mortgage Broker.
My thoughts are the following details on the Front, middle of the card possibly? Phone and email smaller font than my name?
Tessa Marwick
Finance Specialist
p: 0438 217 905
e: tessa@marwickfinance.com.au
Bottom of the card
residential / commercial / equipment
I would like the Font in Rose Gold maybe white or black background? or Possibly a stone grey - are you able to do a few options? I'd like them embossed
Then I had an idea as a simple logo as per the attached if you get the idea in my scribble, my initials, capital T attached to a small m that leads/follows into a circle? Thicker Font In Rose Gold, middle of the card at the back.
Very open to ideas though and what colour you think would look better with the Rose Gold.
Thanks so much for your help, I am not very creative and savvy with this stuff :-)
Industry/Entity Type
Finance
Contact Information for Business Card
Tessa Marwick
p: 0438 217 905
Look and feel
Each slider illustrates characteristics of the customer's brand and the style your logo design should communicate.

```html
<!DOCTYPE html>
<html lang="en">
<head>
<meta charset="utf-8">
<title>Tessa Marwick – Business Cards</title>
<link rel="stylesheet" href="https://fonts.googleapis.com/css2?family=Arimo:ital,wght@0,400;0,700;1,400&display=swap">
<style>
  :root {
    --page-bg: #e4e4e4;
    --card-white: #f6f6f4;
    --card-black: #050505;
    --rose: #9c3f4c;
    --ink: #0d0d0d;
  }
  * { margin: 0; padding: 0; box-sizing: border-box; }
  html, body {
    width: 1200px;
    height: 1200px;
    overflow: hidden;
    background: var(--page-bg);
    font-family: "Arimo", Arial, sans-serif;
  }
  .sheet {
    position: relative;
    width: 1200px;
    height: 1200px;
  }
  .card {
    position: absolute;
    left: 150px;
    width: 900px;
    height: 514px;
    box-shadow: 0 2px 6px rgba(0,0,0,0.12);
  }
  .card--back {
    top: 60px;
    background: var(--card-black);
  }
  .card--front {
    top: 626px;
    background: var(--card-white);
  }

  /* brand mark: plain circle + name */
  .brand {
    position: absolute;
    display: flex;
    align-items: center;
    gap: 18px;
    color: var(--rose);
    font-weight: 700;
    font-style: normal;
  }
  .brand__circle {
    flex: none;
    border: 4px solid var(--rose);
    border-radius: 50%;
  }
  .card--back .brand {
    left: 50%;
    top: 50%;
    transform: translate(-50%, -50%);
    flex-direction: column;
    gap: 26px;
    font-size: 34px;
  }
  .card--back .brand__circle { width: 170px; height: 170px; }

  .card--front .brand {
    left: 80px;
    top: 56px;
    font-size: 22px;
  }
  .card--front .brand__circle { width: 140px; height: 140px; }

  /* contact details */
  .details {
    position: absolute;
    left: 468px;
    top: 188px;
    font-style: italic;
    color: var(--ink);
  }
  .details__name,
  .details__title {
    font-size: 43px;
    line-height: 54px;
    font-weight: 400;
  }
  .details__phone,
  .details__email {
    font-size: 23px;
    line-height: 31px;
  }
  .details__phone { margin-top: 6px; }
  .details__services {
    margin-top: 4px;
    font-size: 23px;
    line-height: 31px;
    color: var(--rose);
  }
</style>
</head>
<body>
  <main class="sheet">
    <section class="card card--back" aria-label="Card back">
      <div class="brand">
        <span class="brand__circle"></span>
        <span class="brand__name">Tessa Marwick Finance</span>
      </div>
    </section>

    <section class="card card--front" aria-label="Card front">
      <div class="brand">
        <span class="brand__circle"></span>
        <span class="brand__name">Marwick Finance</span>
      </div>
      <div class="details">
        <p class="details__name">Tessa Marwick</p>
        <p class="details__title">Finance Specialist</p>
        <p class="details__phone">0438 217 905</p>
        <p class="details__email">tessa@marwickfinance.com.au</p>
        <p class="details__services">Residential / Commercial / Equipment</p>
      </div>
    </section>
  </main>
</body>
</html>
```